Marsh Family Chiropractic Stationary

The letterhead and business card must have our logo.
We would like to see the logo used in different ways ( It can be expanded upon in the stationary.)
Please use the the same or similar colors.
Must be eye catching and memorable.
Must be easy to read

Reason: The doctor has been too busy to make any final decisions. He would like to give himself a little more time.

Target Market(s)

Chiropractic Healthcare

Industry/Entity Type

Business

Requirements
Must have
• Dr. Nathaniel Pruett D.C.
Chiropractor

860-555-0193

417 Larkspur Parkway, 2nd Floor
Vernon, CT 06000

drpruett@marshspinecare.example
www.marshspinecare.example
www.facebook.com/MarshFamilySpine
Should not have
• should not be difficult to read

```html
<!DOCTYPE html>
<html lang="en">
<head>
<meta charset="utf-8">
<title>Marsh Family Chiropractic Stationery</title>
<link rel="stylesheet" href="https://fonts.googleapis.com/css2?family=Questrial&family=Pathway+Gothic+One&display=swap">
<style>
  :root {
    --card-dark: #2b2825;
    --brand-green: #9bd12c;
    --leaf-green: #6cc644;
    --leaf-olive: #a5ab3a;
    --leaf-yellow: #e6f04a;
    --text-grey: #c9c7c3;
    --leaf-grey: #55585a;
    --paper: #ffffff;
    --ink: #2b2825;
    --sheet-line: #333333;
  }
  * { box-sizing: border-box; margin: 0; padding: 0; }
  html, body {
    width: 1200px; height: 880px; overflow: hidden;
    background: var(--paper);
    font-family: "Questrial", "Century Gothic", sans-serif;
  }
  .stationery { position: relative; width: 1200px; height: 880px; }

  /* ---------- business card front ---------- */
  .card-front {
    position: absolute; left: 73px; top: 70px; width: 395px; height: 230px;
    background: var(--card-dark);
    display: flex; flex-direction: column; align-items: center; justify-content: center; gap: 14px;
  }
  .brand-dot { width: 54px; height: 54px; border-radius: 50%; background: var(--brand-green); }
  .brand-name {
    color: var(--brand-green); font-size: 26px; letter-spacing: 1px; text-transform: uppercase;
    text-align: center; line-height: 1.15;
  }

  /* ---------- business card back ---------- */
  .card-back {
    position: absolute; background: var(--card-dark); overflow: hidden;
    font-size: 13px; color: var(--text-grey);
  }
  .card-back.large { left: 73px; top: 310px; width: 395px; height: 230px; }
  .card-back.mini { font-size: 7px; width: 213px; height: 124px; }
  .card-back.mini-top { left: 170px; top: 590px; }
  .card-back.mini-left { left: 54px; top: 721px; }
  .card-back.mini-right { left: 287px; top: 721px; }

  .card-details { position: absolute; left: 1.1em; top: 1.3em; }
  .role {
    font-family: "Pathway Gothic One", "Arial Narrow", sans-serif;
    color: var(--brand-green); font-size: 1.15em; line-height: 1.1;
  }
  .doctor { color: var(--brand-green); font-size: 1.55em; line-height: 1.25; }
  .address { font-size: 0.95em; line-height: 1.35; }
  .contact { margin-top: 1.9em; font-size: 1.15em; line-height: 1.55; }
  .contact .label { color: var(--brand-green); font-size: 1.3em; display: inline-block; width: 1em; }
  .web { margin-top: 1em; font-size: 0.95em; line-height: 1.4; }

  .leaf-art { position: absolute; right: 0; bottom: 0; }
  .large .leaf-art { width: 40%; height: 60%; }
  .mini .leaf-art { width: 38%; height: 85%; }

  /* ---------- letterhead ---------- */
  .letterhead {
    position: absolute; left: 598px; top: 67px; width: 533px; height: 755px;
    border: 1px solid var(--sheet-line); background: var(--paper);
  }
  .letterhead-logo {
    position: absolute; left: 185px; top: 0; width: 165px; height: 123px;
    background: var(--card-dark);
    display: flex; flex-direction: column; align-items: center; justify-content: center; gap: 8px;
  }
  .letterhead-logo .brand-dot { width: 34px; height: 34px; }
  .letterhead-logo .brand-name { font-size: 13px; letter-spacing: 0.5px; }
  .letterhead-title { position: absolute; left: 0; right: 0; top: 129px; text-align: center; }
  .letterhead-title .role { font-size: 11px; }
  .letterhead-title .doctor { font-size: 14px; line-height: 1.2; }
  .letterhead-contact {
    position: absolute; left: 8px; bottom: 14px; color: var(--ink);
    font-size: 10.5px; font-weight: bold; line-height: 1.45;
  }
  .letterhead-contact .label { color: var(--brand-green); }
  .letterhead-art { position: absolute; right: 0; bottom: 0; width: 180px; height: 190px; }
</style>
</head>
<body>
<main class="stationery">

  <section class="card-front">
    <div class="brand-dot"></div>
    <div class="brand-name">Marsh Family Chiropractic</div>
  </section>

  <section class="card-back large">
    <div class="card-details">
      <div class="role">Chiropractor</div>
      <div class="doctor">Dr. Nathaniel Pruett D.C.</div>
      <div class="address">417 Larkspur Parkway, 2nd Floor<br>Vernon, CT 06000</div>
      <div class="contact">
        <div><span class="label">T</span> 860-555-0193</div>
        <div><span class="label">E</span> drpruett@marshspinecare.example</div>
      </div>
      <div class="web">www.marshspinecare.example<br>www.facebook.com/MarshFamilySpine</div>
    </div>
    <svg class="leaf-art" viewBox="0 0 100 100" preserveAspectRatio="none" role="img" aria-label="Scattered leaf decoration in greens and yellows">
      <defs>
        <radialGradient id="leafGlow" cx="80%" cy="80%" r="85%">
          <stop offset="0" stop-color="#8cc63f"/>
          <stop offset="0.55" stop-color="#a5ab3a" stop-opacity="0.6"/>
          <stop offset="1" stop-color="#2b2825" stop-opacity="0"/>
        </radialGradient>
      </defs>
      <rect width="100" height="100" fill="url(#leafGlow)"/>
    </svg>
  </section>

  <section class="card-back mini mini-top">
    <div class="card-details">
      <div class="role">Chiropractor</div>
      <div class="doctor">Dr. Nathaniel Pruett D.C.</div>
      <div class="address">417 Larkspur Parkway, 2nd Floor<br>Vernon, CT 06000</div>
      <div class="contact">
        <div><span class="label">T</span> 860-555-0193</div>
        <div><span class="label">E</span> drpruett@marshspinecare.example</div>
      </div>
      <div class="web">www.marshspinecare.example<br>www.facebook.com/MarshFamilySpine</div>
    </div>
    <svg class="leaf-art" viewBox="0 0 100 100" preserveAspectRatio="none" role="img" aria-label="Scattered grey leaf decoration">
      <defs>
        <radialGradient id="leafGrey" cx="60%" cy="55%" r="60%">
          <stop offset="0" stop-color="#55585a"/>
          <stop offset="1" stop-color="#2b2825" stop-opacity="0"/>
        </radialGradient>
      </defs>
      <rect width="100" height="100" fill="url(#leafGrey)"/>
    </svg>
  </section>

  <section class="card-back mini mini-left">
    <div class="card-details">
      <div class="role">Chiropractor</div>
      <div class="doctor">Dr. Nathaniel Pruett D.C.</div>
      <div class="address">417 Larkspur Parkway, 2nd Floor<br>Vernon, CT 06000</div>
      <div class="contact">
        <div><span class="label">T</span> 860-555-0193</div>
        <div><span class="label">E</span> drpruett@marshspinecare.example</div>
      </div>
      <div class="web">www.marshspinecare.example<br>www.facebook.com/MarshFamilySpine</div>
    </div>
    <svg class="leaf-art" viewBox="0 0 100 100" preserveAspectRatio="none" role="img" aria-label="Scattered leaf decoration in greens and yellows">
      <defs>
        <radialGradient id="leafGlowMini" cx="75%" cy="55%" r="70%">
          <stop offset="0" stop-color="#8cc63f"/>
          <stop offset="0.6" stop-color="#a5ab3a" stop-opacity="0.55"/>
          <stop offset="1" stop-color="#2b2825" stop-opacity="0"/>
        </radialGradient>
      </defs>
      <rect width="100" height="100" fill="url(#leafGlowMini)"/>
    </svg>
  </section>

  <section class="card-back mini mini-right">
    <div class="card-details">
      <div class="role">Chiropractor</div>
      <div class="doctor">Dr. Nathaniel Pruett D.C.</div>
      <div class="address">417 Larkspur Parkway, 2nd Floor<br>Vernon, CT 06000</div>
      <div class="contact">
        <div><span class="label">T</span> 860-555-0193</div>
        <div><span class="label">E</span> drpruett@marshspinecare.example</div>
      </div>
      <div class="web">www.marshspinecare.example<br>www.facebook.com/MarshFamilySpine</div>
    </div>
    <svg class="leaf-art" viewBox="0 0 100 100" preserveAspectRatio="none" role="img" aria-label="Leaf decoration rising from a green hill in the corner">
      <defs>
        <linearGradient id="hillGlow" x1="0" y1="0" x2="1" y2="1">
          <stop offset="0" stop-color="#2b2825" stop-opacity="0"/>
          <stop offset="0.5" stop-color="#a5ab3a" stop-opacity="0.55"/>
          <stop offset="1" stop-color="#8cc63f"/>
        </linearGradient>
      </defs>
      <rect width="100" height="100" fill="url(#hillGlow)"/>
    </svg>
  </section>

  <section class="letterhead">
    <div class="letterhead-logo">
      <div class="brand-dot"></div>
      <div class="brand-name">Marsh Family Chiropractic</div>
    </div>
    <div class="letterhead-title">
      <div class="role">Chiropractor</div>
      <div class="doctor">Dr. Nathaniel Pruett D.C.</div>
    </div>
    <div class="letterhead-contact">
      <div><span class="label">T</span> 860-555-0193</div>
      <div><span class="label">E</span> drpruett@marshspinecare.example</div>
      <div>www.marshspinecare.example</div>
      <div>www.facebook.com/MarshFamilySpine</div>
      <div>417 Larkspur Parkway, 2nd Floor Vernon, CT 06000</div>
    </div>
    <svg class="letterhead-art" viewBox="0 0 100 100" preserveAspectRatio="none" role="img" aria-label="Scattered leaf decoration in greens and yellows">
      <defs>
        <radialGradient id="leafGlowSheet" cx="60%" cy="60%" r="65%">
          <stop offset="0" stop-color="#8cc63f" stop-opacity="0.85"/>
          <stop offset="0.55" stop-color="#e6f04a" stop-opacity="0.5"/>
          <stop offset="1" stop-color="#ffffff" stop-opacity="0"/>
        </radialGradient>
      </defs>
      <rect width="100" height="100" fill="url(#leafGlowSheet)"/>
    </svg>
  </section>

</main>
</body>
</html>
```